Water Filter Company Needs Bizz Cards!!

Need business cards for my company. We sell whole home water filters and salt free water softeners. No more buying bottled water. Our filtering units filter out all heavy metals, chlorine, and VOC's, last 15 years, and are maintenance free and supply your whole home with spring quality alkaline water. Our Salt free water conditioners, eliminate hard water and scale, without lowering the ph, or TDS's (total Dissolved solids)

I think this is the color code we are using on my site. My logo looks good behind it. #192841

Website will be www.Brovexa.com

Industry/Entity Type

Water Purification

Contact Information for Business Card

For now, just insert standard Dummy text. I need these text lines for the info to be editable so i can make them for multiple employees. I do have Photoshop and illustrator, unless there is a simpler program i can use solely for biz cards

Font styles to use
Sans Serif

Requirements
Must have
• Use my preexisting logo.

www.BroVexa.com

Spring Quality Alkaline Water at every tap.

List out services. Whole Home Water Filters, Salt Free Water Softeners, Clarimont KT7, UV Sterilizers
Nice to have
• I think this is the color code we are using on my site. My logo looks good behind it. #192841 or black. Please no white or light blue backgrounds.

Maybe a picture of my tank.

Slogan like Spring Quality Alkaline Water at every tap.
And just list the services Whole Home Water Filters, Salt Free Water Softeners, Clarimont KT7, UV Sterilizers

I think I would like to not have a contrasting textured logo like I see on some of them. I may use it for my personal cards, but new employees may not want the extra expense.
Should not have
• A different logo than the one provided.

White or baby blue backgrounds. Use the color code, or blacks.

```html
<!DOCTYPE html>
<html lang="en">
<head>
<meta charset="utf-8">
<title>Brovexa Business Cards</title>
<link rel="stylesheet" href="https://fonts.googleapis.com/css2?family=Quicksand:wght@400;500;700&family=Oswald:wght@400;500&family=Montserrat:wght@500&display=swap">
<style>
  :root {
    --stage: #1c1d21;
    --navy: #192841;
    --navy-edge: #142136;
    --blue: #1e9be0;
    --text: #e9edf3;
    --muted: #9aa6b8;
  }
  * { margin: 0; padding: 0; box-sizing: border-box; }
  html, body { width: 1200px; height: 900px; overflow: hidden; background: var(--stage); }
  .canvas { position: relative; width: 1200px; height: 900px; }

  .card {
    position: absolute; left: 250px; width: 700px; height: 400px;
    background: var(--navy); overflow: hidden;
    box-shadow: 0 6px 0 var(--navy-edge), 0 18px 40px rgba(0,0,0,.45);
  }
  .card-back { top: 30px; }
  .card-front { top: 470px; }

  .brand { display: flex; align-items: center; gap: 12px; }
  .brand-dot { width: 22px; height: 22px; border-radius: 50%; background: var(--blue); }
  .brand-name { font-family: 'Quicksand', sans-serif; font-weight: 700; color: var(--blue); }

  /* back */
  .card-back .brand { position: absolute; left: 0; right: 0; top: 140px; justify-content: center; }
  .card-back .brand-dot { width: 40px; height: 40px; }
  .card-back .brand-name { font-size: 78px; line-height: 1; }
  .slogan {
    position: absolute; left: 0; right: 0; top: 262px; text-align: center;
    font-family: 'Quicksand', sans-serif; font-size: 20px; color: var(--muted); letter-spacing: .5px;
  }

  /* front */
  .accent { position: absolute; inset: 0; }
  .card-front .brand { position: absolute; left: 90px; top: 50px; }
  .card-front .brand-name { font-size: 40px; line-height: 1; }
  .person { position: absolute; left: 118px; top: 118px; }
  .person-name { font-family: 'Oswald', sans-serif; font-weight: 500; font-size: 44px; color: var(--text); line-height: 1; transform: scaleX(.85); transform-origin: left; }
  .person-role { font-family: 'Quicksand', sans-serif; font-size: 15px; letter-spacing: 11px; color: var(--text); margin-top: 10px; }
  .services {
    position: absolute; left: 90px; top: 262px; width: 285px;
    font-family: 'Montserrat', sans-serif; font-size: 13px; line-height: 1.6;
    color: var(--blue); text-transform: uppercase;
  }
  .divider { position: absolute; left: 0; top: 0; }
  .contact { position: absolute; left: 420px; top: 90px; list-style: none; }
  .contact li {
    display: flex; gap: 14px; align-items: flex-start; margin-bottom: 12px;
    font-family: 'Quicksand', sans-serif; font-weight: 500; font-size: 18px; color: var(--text); line-height: 1.3;
  }
  .contact svg { flex: none; margin-top: 4px; }
</style>
</head>
<body>
<main class="canvas">

  <section class="card card-back" aria-label="Card back">
    <div class="brand">
      <span class="brand-dot"></span>
      <span class="brand-name">Brovexa</span>
    </div>
    <p class="slogan">Spring Quality Alkaline Water at every tap</p>
  </section>

  <section class="card card-front" aria-label="Card front">
    <svg class="accent" width="700" height="400" viewBox="0 0 700 400" aria-hidden="true">
      <path d="M0 0 H62 Q30 110 40 400 H0 Z" fill="var(--blue)"/>
      <circle cx="785" cy="335" r="115" fill="var(--blue)"/>
      <circle cx="770" cy="365" r="100" fill="var(--navy)"/>
      <rect x="692" y="250" width="8" height="150" fill="var(--navy)"/>
    </svg>

    <div class="brand">
      <span class="brand-dot"></span>
      <span class="brand-name">Brovexa</span>
    </div>

    <div class="person">
      <p class="person-name">JOHN SMITH</p>
      <p class="person-role">POSITION</p>
    </div>

    <p class="services">Whole Home Water Filters · Salt Free Water Softeners · Clarimont KT7 · UV Sterilizers</p>

    <svg class="divider" width="700" height="400" viewBox="0 0 700 400" aria-hidden="true">
      <line x1="395" y1="70" x2="395" y2="330" stroke="var(--blue)" stroke-width="2" opacity=".7"/>
    </svg>

    <ul class="contact">
      <li>
        <svg width="16" height="16" viewBox="0 0 16 16"><path d="M4 1 L6.5 4.5 L5 6.5 Q6.5 9.5 9.5 11 L11.5 9.5 L15 12 L13 15 Q5 14 1 3 Z" fill="var(--text)"/></svg>
        <span>+00 000 000 00<br>+00 000 000 00</span>
      </li>
      <li>
        <svg width="16" height="16" viewBox="0 0 16 16"><rect x="1" y="3" width="14" height="10" fill="var(--text)"/><path d="M1 3 L8 9 L15 3" fill="none" stroke="var(--navy)" stroke-width="1.5"/></svg>
        <span>info@yourweb.com</span>
      </li>
      <li>
        <svg width="16" height="16" viewBox="0 0 16 16"><circle cx="8" cy="8" r="6.5" fill="none" stroke="var(--text)" stroke-width="1.5"/><ellipse cx="8" cy="8" rx="3" ry="6.5" fill="none" stroke="var(--text)" stroke-width="1.2"/><line x1="1.5" y1="8" x2="14.5" y2="8" stroke="var(--text)" stroke-width="1.2"/></svg>
        <span>www.yourweb.com</span>
      </li>
      <li>
        <svg width="16" height="16" viewBox="0 0 16 16"><path d="M8 15 Q2 8 2 6 A6 6 0 0 1 14 6 Q14 8 8 15 Z" fill="var(--text)"/><circle cx="8" cy="6" r="2.2" fill="var(--navy)"/></svg>
        <span>address line here,<br>City, State, Country</span>
      </li>
    </ul>
  </section>

</main>
</body>
</html>
```